Facebook Post for Fence Spring Sale

We have a $12 / FT Fence sale that we have been running for a while now. We need a flyer made up for SPRING.

Our previous flyer can be seen here:
https://media.pixvault-host.example/img/48213907_551903288146720_7391026458813302947_n.jpg?ref=7c21b9e04d8a

We want to use the photos that are shown here https://files.cloudtrove-share.example/view?id=9XkQ7rTmw2LpZdVa4HsE in the flyer. This is to be posted on Facebook so it must be the proper size for Facebook page post.

The wording to be used should be "Spring Fence Sale" and "$12 / FT Wood Fences" Also we should include our business name "Oakridge Fence" and phone number for Free Estimates - 555-314-2076.

Residential Construction

Font styles to use
Serif
Sans Serif

Colors
3176b5
fbee3d
fbed22
fbf289
85cae6
33a6d7

Requirements
Must have
• Phone number, $12 / FT Fence Sale

```html
<!DOCTYPE html>
<html lang="en">
<head>
<meta charset="utf-8">
<title>Oakridge Fence – Spring Fence Sale</title>
<link rel="stylesheet" href="https://fonts.googleapis.com/css2?family=Poiret+One&family=Oswald:wght@700&family=Roboto:wght@400;700&display=swap">
<style>
  :root{
    --bg-light:#fbfbe6;
    --bg-mid:#f3f7cf;
    --bg-warm:#f6ecc4;
    --olive:#6b7d10;
    --sale-red:#e2283c;
    --sticker-dark:#4f9317;
    --sticker-light:#8cc63f;
    --estimate-red:#e0262e;
    --ink:#111111;
    --brand-green:#6f8a12;
    --frame:#fbfaf3;
    --blossom:#f39bb0;
  }
  html,body{margin:0;padding:0;overflow:hidden;}
  .canvas{
    position:relative;width:1200px;height:1200px;overflow:hidden;
    background:
      radial-gradient(circle at 45% 45%, var(--bg-light) 0%, var(--bg-mid) 55%, var(--bg-warm) 100%);
    font-family:"Roboto",Arial,sans-serif;
  }
  .blur-blossom{
    position:absolute;left:-60px;top:-40px;width:320px;height:300px;border-radius:50%;
    background:radial-gradient(circle, rgba(240,110,120,.75) 0%, rgba(245,150,150,.35) 45%, rgba(250,230,200,0) 72%);
    filter:blur(10px);
  }
  .headline{position:absolute;left:0;top:0;width:1200px;height:700px;}
  .headline text{font-family:"Poiret One","Josefin Sans",sans-serif;}
  .headline .word-spring,.headline .word-fence{fill:var(--olive);}
  .headline .word-sale{fill:var(--sale-red);}
  .blossom-branch{
    position:absolute;left:715px;top:85px;width:485px;height:330px;
    background:
      radial-gradient(ellipse at 40% 55%, rgba(243,155,176,.9) 0%, rgba(243,155,176,.5) 30%, rgba(150,200,90,.35) 55%, rgba(150,200,90,0) 75%);
    border-radius:45% 40% 50% 55%;
  }
  .sticker{position:absolute;left:95px;top:665px;width:350px;height:350px;}
  .sticker text{font-family:"Oswald","Anton",sans-serif;fill:#fff;font-weight:700;}
  .estimates{
    position:absolute;left:66px;top:1050px;margin:0;
    font-size:34px;color:var(--estimate-red);letter-spacing:.5px;font-weight:400;
  }
  .phone{
    position:absolute;left:62px;top:1082px;margin:0;
    font-size:78px;font-weight:700;color:var(--ink);letter-spacing:-1px;
  }
  .brand{
    position:absolute;left:848px;top:1110px;margin:0;
    font-size:32px;color:var(--brand-green);letter-spacing:2px;font-weight:400;
    border-bottom:2px solid var(--brand-green);padding-bottom:2px;line-height:1;
  }
  .polaroid{
    position:absolute;background:var(--frame);padding:14px 14px 34px;box-sizing:border-box;
    box-shadow:2px 6px 14px rgba(60,50,20,.35);
  }
  .polaroid .photo{width:100%;height:100%;}
  .photo.rail{background:linear-gradient(180deg,#8fae5a 0%,#6f9a3a 45%,#c8b077 100%);}
  .photo.spaced{background:linear-gradient(180deg,#3e5a2e 0%,#6b8f44 50%,#d9c48a 100%);}
  .photo.picket{background:linear-gradient(180deg,#c9d2c4 0%,#9db56c 40%,#e6d39a 100%);}
  .photo.scallop{background:linear-gradient(180deg,#a7b2b8 0%,#d4b36a 45%,#b98f3f 100%);}
  .photo.privacy{background:linear-gradient(180deg,#8c3a2c 0%,#e2c98c 35%,#d8b672 100%);}
  .p1{left:580px;top:618px;width:275px;height:250px;transform:rotate(12deg);}
  .p2{left:870px;top:575px;width:285px;height:230px;transform:rotate(-8deg);}
  .p3{left:790px;top:745px;width:220px;height:290px;transform:rotate(-3deg);}
  .p4{left:960px;top:710px;width:225px;height:320px;transform:rotate(11deg);}
  .p5{left:515px;top:838px;width:290px;height:320px;transform:rotate(-6deg);}
</style>
</head>
<body>
<div class="canvas">
  <div class="blur-blossom" role="img" aria-label="Soft out-of-focus pink blossom"></div>

  <svg class="headline" viewBox="0 0 1200 700" aria-label="Spring Fence Sale">
    <text class="word-sale" x="69" y="638" font-size="560" textLength="969" lengthAdjust="spacingAndGlyphs">Sale</text>
    <text class="word-spring" x="331" y="175" font-size="128" textLength="350" lengthAdjust="spacingAndGlyphs">Spring</text>
    <text class="word-fence" x="338" y="322" font-size="118" textLength="318" lengthAdjust="spacingAndGlyphs">Fence</text>
  </svg>

  <div class="blossom-branch" role="img" aria-label="Pink blossom branch with a monarch butterfly"></div>

  <svg class="sticker" viewBox="0 0 350 350" aria-label="$12 per foot wood fences">
    <defs>
      <linearGradient id="stickerFill" x1="0" y1="0" x2="1" y2="1">
        <stop offset="0" stop-color="var(--sticker-light)"/>
        <stop offset="1" stop-color="var(--sticker-dark)"/>
      </linearGradient>
    </defs>
    <circle cx="172" cy="172" r="165" fill="#ffffff" opacity=".95"/>
    <circle cx="172" cy="172" r="152" fill="url(#stickerFill)"/>
    <path d="M250 300 Q300 285 335 230 Q322 300 262 332 Z" fill="#f4f1e4"/>
    <path d="M250 300 Q300 285 335 230" fill="none" stroke="#d8d4c0" stroke-width="2"/>
    <g transform="rotate(-30 172 172)">
      <text x="172" y="178" font-size="88" text-anchor="middle">$12/ft</text>
      <text x="172" y="236" font-size="46" text-anchor="middle">Wood Fences</text>
    </g>
  </svg>

  <div class="polaroid p1"><div class="photo rail" role="img" aria-label="Split rail wood fence with wire mesh on a lawn"></div></div>
  <div class="polaroid p2"><div class="photo spaced" role="img" aria-label="Spaced picket fence gate beside trees"></div></div>
  <div class="polaroid p3"><div class="photo picket" role="img" aria-label="Scalloped picket fence along a yard"></div></div>
  <div class="polaroid p4"><div class="photo scallop" role="img" aria-label="Concave privacy fence near houses"></div></div>
  <div class="polaroid p5"><div class="photo privacy" role="img" aria-label="Arched wood privacy fence beside a brick house"></div></div>

  <p class="estimates">FOR FREE ESTIMATES</p>
  <p class="phone">555-314-2076</p>
  <p class="brand">OAKRIDGE FENCE</p>
</div>
</body>
</html>
```